Where's my Gym Buddy? looking to do two promotions as listed in project description

looking for two designs.

1: selfie frame design!! (wording) Frost Grind Carnival, my Summer fitness has started, Tag a friend who should be joining me. T.C Tag your posts to @brightloopsydney to win points for the competition. (Snow graphic) in a selfie frame design. this needs to be the same design but across different departments as seen at the top of the photo's I've attached EG: #brightloopfitness #brightloopindoor #brightloopswim #brightloopwyong

2: Selfie Frame Design!! (Wording) Where's my gym buddy?, Tag a friend who should be at the gym, T.C.Tag your posts to @brightloopsydney to win points for the competition. Spot the Pilot Feel Selfie frame design

Target Market(s)

Gym Members

Industry/Entity Type

Gym

Colors

Designer to choose colors to be used in the design.

Requirements
Must have
• quirky and funky design, must include wording listed, must be a selfie frame design
Should not have
• whilst we are a big corporate gym, we pride ourselves on having really funky advertisements, so please no boring business corporate typical designs

```html
<!DOCTYPE html>
<html lang="en">
<head>
<meta charset="utf-8">
<title>Frost Grind Carnival – Selfie Frame</title>
<link rel="stylesheet" href="https://fonts.googleapis.com/css2?family=Arvo:wght@700&family=Baloo+2:wght@700&family=Bowlby+One&family=Noto+Serif&display=swap">
<style>
  :root {
    --stage: #d9dde0;
    --sky-top: #a7cbd6;
    --sky-mid: #c9e1e9;
    --sky-low: #f2f8fb;
    --snow-soft: rgba(255, 255, 255, 0.55);
    --snow-faint: rgba(255, 255, 255, 0.3);
    --ink: #1d3a44;
    --teal: #1d7c8a;
    --teal-dark: #125562;
    --teal-deep: #0c3f49;
    --frame-light: #3fb4cc;
    --frame-dark: #17707f;
    --white: #ffffff;
    --muted: #2f5864;
    --rule: #4f8c99;
  }
  * { margin: 0; padding: 0; box-sizing: border-box; }
  html, body { width: 900px; height: 1200px; overflow: hidden; }
  body { background: var(--stage); position: relative; font-family: "Noto Serif", Georgia, serif; }

  .poster {
    position: absolute; left: 97px; top: 102px; width: 708px; height: 1000px;
    background: linear-gradient(180deg, var(--sky-top) 0%, var(--sky-mid) 45%, var(--sky-low) 80%, var(--white) 100%);
    overflow: hidden;
  }
  .snowfall {
    position: absolute; inset: 0;
    background:
      radial-gradient(circle at 8% 22%, var(--snow-soft) 0, transparent 60px),
      radial-gradient(circle at 30% 10%, var(--snow-faint) 0, transparent 70px),
      radial-gradient(circle at 58% 4%, var(--snow-soft) 0, transparent 50px),
      radial-gradient(circle at 88% 14%, var(--snow-faint) 0, transparent 80px),
      radial-gradient(circle at 4% 44%, var(--snow-soft) 0, transparent 55px),
      radial-gradient(circle at 96% 40%, var(--snow-soft) 0, transparent 65px),
      radial-gradient(circle at 6% 62%, var(--snow-faint) 0, transparent 60px),
      radial-gradient(circle at 95% 58%, var(--snow-faint) 0, transparent 55px),
      radial-gradient(circle at 20% 30%, var(--snow-faint) 0, transparent 40px),
      radial-gradient(circle at 78% 28%, var(--snow-soft) 0, transparent 45px),
      radial-gradient(circle at 45% 20%, var(--snow-faint) 0, transparent 90px);
  }
  .shapes { position: absolute; left: 0; top: 0; width: 900px; height: 1200px; }

  .hashtag {
    position: absolute; left: 97px; width: 708px; top: 138px; text-align: center;
    font-family: "Baloo 2", "Trebuchet MS", sans-serif; font-weight: 700;
    font-size: 43px; line-height: 56px; color: var(--ink);
  }
  .event-title {
    position: absolute; left: 97px; width: 708px; top: 207px; text-align: center;
    font-family: "Bowlby One", Impact, sans-serif; font-size: 46px; line-height: 70px; font-weight: 400;
    color: var(--white); letter-spacing: 0.5px;
    -webkit-text-stroke: 2px var(--ink);
    text-shadow: 3px 4px 0 var(--ink);
  }
  .ribbon-text {
    position: absolute; text-align: center; color: var(--white);
    font-family: "Arvo", Georgia, serif; font-weight: 700;
  }
  .ribbon-text.top { left: 178px; width: 547px; top: 305px; font-size: 27px; line-height: 40px; }
  .ribbon-text.bottom { left: 160px; width: 585px; top: 961px; font-size: 19px; line-height: 32px; }

  .photo-frame { position: absolute; left: 184px; top: 380px; width: 532px; height: 513px; }
  .photo-window { position: absolute; left: 209px; top: 402px; width: 483px; height: 408px; background: var(--white); }

  .call-to-action {
    position: absolute; left: 97px; width: 708px; top: 919px; text-align: center;
    font-family: "Arvo", Georgia, serif; font-weight: 700; font-size: 28px; line-height: 36px;
    color: var(--teal);
  }

  .social { position: absolute; top: 1017px; width: 260px; text-align: center; color: var(--muted); }
  .social.left { left: 190px; }
  .social.right { left: 452px; }
  .social-name { font-size: 14px; line-height: 26px; display: flex; justify-content: center; align-items: center; gap: 6px; }
  .mark { display: inline-block; width: 14px; height: 14px; background: var(--teal-dark); }
  .mark.round { border-radius: 50%; }
  .social-handle { font-size: 19px; line-height: 32px; }
  .divider { position: absolute; left: 451px; top: 1012px; width: 1.5px; height: 60px; background: var(--rule); }
</style>
</head>
<body>
  <div class="poster" role="img" aria-label="Soft icy blue sky with falling snowflakes and stars">
    <div class="snowfall"></div>
  </div>

  <svg class="shapes" viewBox="0 0 900 1200" aria-hidden="true">
    <polygon points="125,316 205,316 205,366 125,366 142,341" fill="var(--teal)"/>
    <polygon points="700,316 772,316 755,341 772,366 700,366" fill="var(--teal)"/>
    <polygon points="178,352 205,366 205,352" fill="var(--teal-deep)"/>
    <polygon points="725,352 700,366 700,352" fill="var(--teal-deep)"/>
    <rect x="178" y="302" width="547" height="50" fill="var(--teal-dark)"/>
    <polygon points="135,955 770,955 748,977 770,999 135,999 157,977" fill="var(--teal)"/>
  </svg>

  <svg class="photo-frame" viewBox="0 0 532 513" role="img" aria-label="Teal selfie frame scattered with white snowflakes">
    <defs>
      <linearGradient id="frameTone" x1="0" y1="0" x2="1" y2="1">
        <stop offset="0" stop-color="var(--frame-dark)"/>
        <stop offset="0.5" stop-color="var(--frame-light)"/>
        <stop offset="1" stop-color="var(--frame-dark)"/>
      </linearGradient>
      <radialGradient id="frost">
        <stop offset="0" stop-color="#ffffff" stop-opacity="0.45"/>
        <stop offset="1" stop-color="#ffffff" stop-opacity="0"/>
      </radialGradient>
    </defs>
    <rect width="532" height="513" fill="url(#frameTone)"/>
    <ellipse cx="130" cy="470" rx="140" ry="45" fill="url(#frost)"/>
    <ellipse cx="400" cy="470" rx="150" ry="45" fill="url(#frost)"/>
    <ellipse cx="14" cy="200" rx="20" ry="140" fill="url(#frost)"/>
    <ellipse cx="518" cy="300" rx="20" ry="140" fill="url(#frost)"/>
  </svg>
  <div class="photo-window"></div>

  <div class="hashtag">#brightloopfitness</div>
  <h1 class="event-title">FROST GRIND CARNIVAL</h1>
  <p class="ribbon-text top">My Summer fitness has started</p>

  <p class="call-to-action">Tag a friend who should be joining me</p>
  <p class="ribbon-text bottom">posts to our pages to win points for the competition</p>

  <div class="social left">
    <div class="social-name"><span class="mark"></span>Sociable</div>
    <div class="social-handle">@brightloopsydney</div>
  </div>
  <div class="divider"></div>
  <div class="social right">
    <div class="social-name"><span class="mark round"></span>PhotoLoop</div>
    <div class="social-handle">@brightloopsydney</div>
  </div>
</body>
</html>
```